Business Card Design for Boutique Agriculture Consulting Practice

Develop a modern Business card design using uploaded logos . Using the color specs 6C344F rgb(108, 52, 79) The fonts are trajan pro and eurostile. The business owner is a woman and should have a hint of femininity. This is what is behind the naming of the company: Rock roads are synonymous with the rural US landscape, where the corn grows and the cattle graze or for Hollow Creek Consulting home. But don’t let the dust get in your eyes, rock roads have edge and are often the only path to a spectacular destination. To navigate them one must know where they are going, have the courage to take a new path and the willingness to adjust their plans to get there.
Target Market(s)
Marketing Professionals
Industry/Entity Type
Agriculture
Contact Information for Business Card
Marisella Duvane
Title: Founder and CEO
Address: 20847 Pellman Lane, Olathe Kansas 66074
Email: md@hollowcreekadvisory.example
Phone: 428.615.2940
Website: www.hollowcreekadvisory.example
Font styles to use
Other font styles liked:
- trajan pro and eurostile
Requirements
Must have
- Please use the correct color specs. Logo color specs are 6C344F rgb(108, 52, 79) The fonts are trajan pro and eurostile. Name, email and phone be the most important information included on the card
Should not have
- additional graphics

```html
<!DOCTYPE html>
<html lang="en">
<head>
<meta charset="utf-8">
<title>Hollow Creek Consulting – Business Card</title>
<link href="https://fonts.googleapis.com/css2?family=Cinzel:wght@400;600&family=Exo:wght@400&display=swap" rel="stylesheet">
<style>
  :root {
    --plum: #6C344F;
    --ink: #2b2b2b;
    --paper: #ffffff;
    --backdrop: #ecebe8;
    --card-shadow: rgba(0, 0, 0, 0.22);
  }
  * { box-sizing: border-box; margin: 0; padding: 0; }
  html, body {
    width: 1200px; height: 900px; overflow: hidden;
    background: var(--backdrop);
  }
  .stage { position: relative; width: 1200px; height: 900px; }
  .card {
    position: absolute; top: 150px; width: 343px; height: 600px;
    box-shadow: 4px 5px 8px var(--card-shadow);
    text-align: center;
  }
  .card--front { left: 246px; background: var(--paper); }
  .card--back  { left: 611px; background: var(--plum); }

  .brand {
    position: absolute; left: 0; right: 0;
    display: flex; flex-direction: column; align-items: center; gap: 12px;
    font-family: "Cinzel", serif; font-weight: 600;
    font-size: 24px; line-height: 1.15; letter-spacing: 1px;
  }
  .brand__dot { width: 14px; height: 14px; border-radius: 50%; }
  .card--front .brand { top: 62px; color: var(--plum); }
  .card--front .brand__dot { background: var(--plum); }
  .card--back .brand { top: 248px; color: var(--paper); }
  .card--back .brand__dot { background: var(--paper); }

  .person__name {
    position: absolute; top: 284px; left: 0; right: 0;
    font-family: "Cinzel", serif; font-weight: 400;
    font-size: 23px; color: var(--plum); letter-spacing: 0.5px;
  }
  .person__title, .address, .contact, .back-web {
    font-family: "Exo", sans-serif; font-weight: 400;
  }
  .person__title {
    position: absolute; top: 313px; left: 0; right: 0;
    font-size: 18px; color: var(--ink);
  }
  .rule-short {
    position: absolute; top: 354px; left: 148px;
    width: 47px; height: 2px; background: var(--plum);
  }
  .address {
    position: absolute; top: 379px; left: 0; right: 0;
    font-size: 18px; line-height: 23px; color: var(--ink);
  }
  .icon-row {
    position: absolute; top: 444px; left: 41px; width: 261px; height: 16px;
    display: flex; align-items: center; justify-content: space-between;
  }
  .icon-row__line { width: 86px; height: 2px; background: var(--plum); }
  .icon-row__icons { display: flex; gap: 10px; align-items: center; }
  .icon-row__icons svg { width: 14px; height: 14px; }
  .contact {
    position: absolute; top: 477px; left: 0; right: 0;
    font-size: 17px; line-height: 23px; color: var(--ink);
  }
  .back-web {
    position: absolute; top: 524px; left: 0; right: 0;
    font-size: 17px; color: var(--paper);
  }
</style>
</head>
<body>
<main class="stage">
  <section class="card card--front">
    <div class="brand"><span class="brand__dot"></span><span>Hollow Creek<br>Consulting</span></div>
    <h1 class="person__name">Marisella Duvane</h1>
    <p class="person__title">Founder and CEO</p>
    <div class="rule-short"></div>
    <p class="address">Address: 20847 Pellman Lane,<br>Olathe Kansas 66074</p>
    <div class="icon-row">
      <span class="icon-row__line"></span>
      <span class="icon-row__icons">
        <svg viewBox="0 0 16 16" aria-label="Phone"><path d="M4 1.5l2.2 3-1.3 1.4c.8 2 2.2 3.6 4.3 4.8l1.4-1.3 3 2.1-1.4 2.3C7.5 13.3 3 8.8 2 3z" fill="none" stroke="#6C344F" stroke-width="1.3" stroke-linejoin="round"/></svg>
        <svg viewBox="0 0 16 16" aria-label="Email"><rect x="1" y="3.5" width="14" height="9" fill="none" stroke="#6C344F" stroke-width="1.2"/><path d="M1 3.5l7 5.5 7-5.5M1 12.5l5-4.5M15 12.5l-5-4.5" fill="none" stroke="#6C344F" stroke-width="1.1"/></svg>
        <svg viewBox="0 0 16 16" aria-label="Website"><circle cx="8" cy="8" r="6.5" fill="none" stroke="#6C344F" stroke-width="1.2"/><ellipse cx="8" cy="8" rx="3" ry="6.5" fill="none" stroke="#6C344F" stroke-width="1"/><path d="M1.5 8h13M2.5 4.8h11M2.5 11.2h11" stroke="#6C344F" stroke-width="1"/></svg>
      </span>
      <span class="icon-row__line"></span>
    </div>
    <p class="contact">428.615.2940<br>md@hollowcreekadvisory.example<br>www.hollowcreekadvisory.example</p>
  </section>

  <section class="card card--back">
    <div class="brand"><span class="brand__dot"></span><span>Hollow Creek<br>Consulting</span></div>
    <p class="back-web">www.hollowcreekadvisory.example</p>
  </section>
</main>
</body>
</html>
```